We need a new business card that reflects who we are. Professional, classy, modern, and service ori

We need a business card design for a window coverings design company in Kansas City called Bright Lane Interiors. We offer professional, modern, and high quality window covering products. We are looking to portray an image of a big, national franchise. We are a 5 location (with showrooms) business with 10 professional designers and 4 professional installers. These cards will be used with Thank you cards, given to realtors, and asked for referrals with.

Target Market(s)

Kansas City

Industry/Entity Type

Business

Contact Information for Business Card

We would like our card to look clean and simple on the front, featuring our logo and Marlow Fenwick's. Our designers' phone numbers and emails should be displayed as well as their title.

Font styles to use
Sans Serif

Colors

Designer to choose colors to be used in the design.

Requirements
Must have
• Front - Logos, name, phone number, email address
• Back - Showroom locations, social media? Appt date/time?
Nice to have
• I would like a clean and modern look (not contemporary. I like a white background, but I am open to ideas. Looking for a "National chain" look for a small business.
Should not have
• Too much busyness.

```html
<!DOCTYPE html>
<html lang="en">
<head>
<meta charset="utf-8">
<title>Bright Lane Interiors – Business Card</title>
<link href="https://fonts.googleapis.com/css2?family=Roboto:wght@400;500;700&family=Roboto+Condensed:wght@400;500;700&display=swap" rel="stylesheet">
<style>
  :root {
    --backdrop: #2b2b2b;
    --card: #f2f2f2;
    --accent: #c9414b;
    --ink: #111111;
    --text: #444444;
    --muted: #5a6068;
    --white: #ffffff;
  }
  * { margin: 0; padding: 0; box-sizing: border-box; }
  html, body { width: 1200px; height: 960px; overflow: hidden; }
  body {
    background: var(--backdrop);
    position: relative;
    font-family: "Roboto", Arial, sans-serif;
  }
  .card {
    position: absolute;
    width: 600px;
    height: 342px;
    background: var(--card);
    box-shadow: 0 3px 6px rgba(0,0,0,0.45);
    overflow: hidden;
  }
  .card--front { left: 322px; top: 108px; }
  .card--back { left: 320px; top: 493px; }

  /* Front */
  .brand {
    position: absolute;
    right: 28px;
    top: 70px;
    text-align: right;
  }
  .brand__name {
    display: flex;
    align-items: center;
    justify-content: flex-end;
    gap: 8px;
    font-size: 23px;
    font-weight: 500;
    color: var(--ink);
    letter-spacing: 0.3px;
  }
  .brand__mark { width: 16px; height: 16px; background: var(--accent); }
  .brand__tagline {
    margin-top: 8px;
    font-size: 12px;
    color: var(--ink);
  }
  .person {
    position: absolute;
    left: 31px;
    top: 200px;
  }
  .person__name {
    font-family: "Roboto Condensed", Arial, sans-serif;
    font-size: 25px;
    font-weight: 500;
    color: var(--accent);
    line-height: 28px;
  }
  .person__title {
    font-size: 15px;
    font-weight: 500;
    color: var(--ink);
    line-height: 18px;
  }
  .contact { margin-top: 12px; list-style: none; }
  .contact__item {
    display: flex;
    align-items: center;
    gap: 7px;
    font-size: 14px;
    color: var(--text);
    line-height: 19px;
  }
  .contact__icon { width: 13px; height: 13px; fill: var(--accent); }
  .web-band {
    position: absolute;
    left: 0;
    bottom: 0;
    width: 348px;
    height: 32px;
  }
  .web-band svg { position: absolute; inset: 0; }
  .web-band__text {
    position: absolute;
    left: 28px;
    top: 7px;
    font-size: 14px;
    color: var(--white);
    letter-spacing: 2.2px;
  }

  /* Back */
  .partner {
    position: absolute;
    top: 40px;
    left: 0;
    width: 100%;
    text-align: center;
    font-size: 15px;
    font-weight: 500;
    color: var(--muted);
  }
  .appointments { position: absolute; left: 82px; top: 82px; list-style: none; }
  .appointments__row {
    display: flex;
    align-items: baseline;
    height: 45.5px;
    color: var(--accent);
    font-size: 17px;
  }
  .appointments__blank {
    display: inline-block;
    border-bottom: 1.5px dotted #8a8a8a;
    margin: 0 3px 0 5px;
    height: 1px;
  }
  .appointments__blank--date { width: 167px; }
  .appointments__blank--time { width: 106px; }
  .appointments__ampm { font-size: 13px; margin-left: 2px; }
  .showrooms {
    position: absolute;
    top: 259px;
    left: 0;
    width: 100%;
    text-align: center;
  }
  .showrooms__heading {
    font-size: 15px;
    font-weight: 700;
    color: var(--accent);
  }
  .showrooms__list {
    margin-top: 4px;
    font-family: "Roboto Condensed", Arial, sans-serif;
    font-size: 13.5px;
    color: var(--text);
  }
  .social {
    margin-top: 7px;
    display: flex;
    justify-content: center;
    gap: 3px;
    list-style: none;
  }
  .social__item { width: 20px; height: 20px; border-radius: 50%; background: var(--accent); }
</style>
</head>
<body>
  <section class="card card--front" aria-label="Business card front">
    <div class="brand">
      <div class="brand__name"><span class="brand__mark"></span>Bright Lane Interiors</div>
      <div class="brand__tagline">Blinds, Shades, Shutters, Draperies &amp; Decor</div>
    </div>
    <div class="person">
      <h1 class="person__name">DANIEL REYES</h1>
      <p class="person__title">DESIGNER</p>
      <ul class="contact">
        <li class="contact__item">
          <svg class="contact__icon" viewBox="0 0 24 24" aria-hidden="true"><path d="M6.6 10.8a15.1 15.1 0 0 0 6.6 6.6l2.2-2.2c.3-.3.7-.4 1-.2 1.1.4 2.3.6 3.6.6.6 0 1 .4 1 1V20c0 .6-.4 1-1 1A17 17 0 0 1 3 4c0-.6.4-1 1-1h3.5c.6 0 1 .4 1 1 0 1.3.2 2.5.6 3.6.1.3 0 .7-.2 1z"/></svg>
          913.555.0148
        </li>
        <li class="contact__item">
          <svg class="contact__icon" viewBox="0 0 24 24" aria-hidden="true"><path d="M2 5h20v14H2z M2 5l10 7 10-7" stroke="#f2f2f2" stroke-width="1.5"/></svg>
          info@brightlaneinteriors.com
        </li>
      </ul>
    </div>
    <div class="web-band">
      <svg width="348" height="32" viewBox="0 0 348 32" aria-hidden="true"><polygon points="0,0 318,0 348,32 0,32" fill="var(--accent)"/></svg>
      <span class="web-band__text">www.brightlaneinteriors.com</span>
    </div>
  </section>

  <section class="card card--back" aria-label="Business card back">
    <p class="partner">Marlow Fenwick Gallery</p>
    <ul class="appointments">
      <li class="appointments__row">Date :<span class="appointments__blank appointments__blank--date"></span>Time :<span class="appointments__blank appointments__blank--time"></span><span class="appointments__ampm">AM/PM</span></li>
      <li class="appointments__row">Date :<span class="appointments__blank appointments__blank--date"></span>Time :<span class="appointments__blank appointments__blank--time"></span><span class="appointments__ampm">AM/PM</span></li>
      <li class="appointments__row">Date :<span class="appointments__blank appointments__blank--date"></span>Time :<span class="appointments__blank appointments__blank--time"></span><span class="appointments__ampm">AM/PM</span></li>
      <li class="appointments__row">Date :<span class="appointments__blank appointments__blank--date"></span>Time :<span class="appointments__blank appointments__blank--time"></span><span class="appointments__ampm">AM/PM</span></li>
    </ul>
    <div class="showrooms">
      <h2 class="showrooms__heading">SHOWROOM LOCATIONS</h2>
      <p class="showrooms__list">RIVERSIDE | OAK HOLLOW | CEDAR RIDGE | NORTHGATE | WESTFIELD</p>
      <ul class="social" aria-label="Social media">
        <li class="social__item"></li>
        <li class="social__item"></li>
        <li class="social__item"></li>
        <li class="social__item"></li>
      </ul>
    </div>
  </section>
</body>
</html>
```